Candle Labels for 9 oz tumbler soy candles

Looking for new label design for my candle business. Currently, using a label I designed that needs to be more professional rather than looking homemade. Wanting a professional, clean looking label that enhances my product line. My candle tumblers are white and at times I also use tin containers for my candles so wanting something that will provide a modern/elegant feel to them

Industry/Entity Type

Business

Font styles to use
Decorative
Script

Colors

Designer to choose colors to be used in the design.

Requirements
Must have
• My logo, net weight 9 oz, Space for the name of the Candle (one example is Amber Hollow
• Looking for something sleek and clean looking, no clutter
Nice to have
• website url www.8brook5candleco.shopvale.com, words "Soy Candle" on the label

```html
<!DOCTYPE html>
<html lang="en">
<head>
<meta charset="utf-8">
<title>Soy Candle Labels</title>
<link rel="stylesheet" href="https://fonts.googleapis.com/css2?family=Cinzel+Decorative:wght@700&family=Cormorant+SC:wght@600&family=Cormorant+Garamond:wght@500&display=swap">
<style>
  :root {
    --page: #f4f3f1;
    --label: #ffffff;
    --rim: #d9d9d9;
    --ink: #2a2a2a;
    --soft-ink: #555555;
    --amber: #e3b33f;
    --frost: #8fb8cc;
    --pine: #8dbfae;
  }
  * { box-sizing: border-box; margin: 0; padding: 0; }
  html, body { width: 1200px; height: 923px; overflow: hidden; }
  body {
    background: var(--page);
    display: flex;
    align-items: center;
    justify-content: center;
    gap: 60px;
  }
  .label {
    width: 320px;
    height: 320px;
    border-radius: 50%;
    background: var(--label);
    border: 10px solid var(--rim);
    overflow: hidden;
    display: flex;
    flex-direction: column;
    align-items: center;
    box-shadow: 0 6px 18px rgba(0,0,0,0.08);
  }
  .brand {
    margin-top: 50px;
    font-family: "Cormorant Garamond", serif;
    font-weight: 500;
    font-size: 24px;
    line-height: 1.1;
    color: var(--ink);
  }
  .kind {
    margin-top: 6px;
    font-family: "Cormorant SC", serif;
    font-weight: 600;
    font-size: 17px;
    letter-spacing: 2px;
    color: var(--ink);
  }
  .scent {
    margin-top: 10px;
    width: 100%;
    height: 92px;
    display: flex;
    align-items: center;
    justify-content: center;
    text-align: center;
    font-family: "Cinzel Decorative", serif;
    font-weight: 700;
    font-size: 26px;
    line-height: 1.05;
    color: var(--ink);
  }
  .scent--amber { background: var(--amber); }
  .scent--frost { background: var(--frost); }
  .scent--pine { background: var(--pine); }
  .weight {
    margin-top: 10px;
    font-family: "Cormorant Garamond", serif;
    font-size: 14px;
    color: var(--soft-ink);
  }
  .url {
    margin-top: 3px;
    font-family: "Cormorant Garamond", serif;
    font-size: 11.5px;
    color: var(--soft-ink);
  }
</style>
</head>
<body>
  <div class="label">
    <div class="brand">Brookvale Co.</div>
    <div class="kind">Soy Candle</div>
    <div class="scent scent--amber">Amber<br>Hollow</div>
    <div class="weight">Net Weight 9 Oz</div>
    <div class="url">www.8brook5candleco.shopvale.com</div>
  </div>
  <div class="label">
    <div class="brand">Brookvale Co.</div>
    <div class="kind">Soy Candle</div>
    <div class="scent scent--frost">Frost<br>Meadow</div>
    <div class="weight">Net Weight 9 Oz</div>
    <div class="url">www.8brook5candleco.shopvale.com</div>
  </div>
  <div class="label">
    <div class="brand">Brookvale Co.</div>
    <div class="kind">Soy Candle</div>
    <div class="scent scent--pine">Cedar &amp;<br>Berry</div>
    <div class="weight">Net Weight 9 Oz</div>
    <div class="url">www.8brook5candleco.shopvale.com</div>
  </div>
</body>
</html>
```